Design of Nail Polish Bottles. VIRA Brand

Design Brief for Vira Nail Polish Bottles
Company Overview:
Vira is a vibrant, emerging nail polish brand that embodies the spirit of holidays, relaxation, and joyful living. Inspired by the warmth and beauty of Southern countries, Vira aims to bring the essence of summer vacations, laughter, and sunny climates into everyday life through its unique nail polish collection.
Project Overview:
We are seeking innovative designs for our new line of nail polish bottles that reflect Vira's brand ethos. The design should capture the lively, upbeat spirit of a holiday in a Southern locale, using vivid colors, playful patterns, and cultural motifs. (Print directly on glass, NOT STICKER)
Bottle Dimensions:
The nail polish bottles have the following dimensions: Height 33mm, Width 31mm, Depth 21mm. Detailed images with dimensions are provided in the attached files to assist in the design process.
Target Audience:
Our primary audience consists of young beauty enthusiasts, particularly women aged 18-35, who enjoy expressing their style and mood through nail art. They are drawn to high-quality, affordable products that offer a sense of escapism and fun.
Design Requirements:
The bottle is rectangular in shape, reflecting the specified dimensions.
The design should incorporate vibrant, eye-catching colors with elements inspired by Mexican, Spanish, and overall Southern patterns or mandalas.
"Vira" should be prominently displayed on the bottle, either symmetrically or shifted to one side, complementing the overall design.
Graphic elements can be located on the front (A), and if necessary sides (B) but must not wrap around the edges due to printing limitations (1-2 mm to edge).
The cap of the bottle can also feature design elements, enhancing the overall aesthetic.
The design should evoke feelings of lightness, sunshine, holidays, laughter, and the cheerful lifestyle of Southern climates.
UPDATES:
To clarify - We do not have a logo that we impose. There should only be an inscription that should be incorporated into the packaging as best as possible. We leave the creation of the style to the creator.
IMPORTANT INFORMATION - the bottle background can be any color! Awere a gradient of two colors (top-bottom) if it necessary.
Updates
Notes on the brief:
- Bottle color (the background can be any color, not just black)
- We do not follow the strict rules of Mexican folk ornaments. The design is intended to evoke the feeling of a Mexican holiday, not to create strictly national symbols.
- It cannot be a minimalist style, subtle forms, but an explosion of colors and energy. Later advertisements will be full of emotions and colors, so the packaging cannot be "bland".
Colorful mosaics or ornaments would be best, although this is not a requirement, we leave the decision to the author.

```html
<!DOCTYPE html>
<html lang="en">
<head>
<meta charset="UTF-8">
<title>Vira Nail Polish Bottle</title>
<link rel="stylesheet" href="https://fonts.googleapis.com/css2?family=Kaushan+Script&display=swap">
<style>
  :root {
    --canvas-bg: #e9e9e9;
    --cap-black: #1c1c1c;
    --cap-line: #e23ad8;
    --body-pink: #c7357f;
    --body-pink-light: #d44590;
    --title-orange: #ec7a22;
    --band-purple: #4a2a78;
    --band-coral: #e04f38;
    --band-teal: #6fbfa6;
    --band-orange: #ef8a3c;
  }
  html, body {
    margin: 0;
    padding: 0;
    width: 1002px;
    height: 1200px;
    overflow: hidden;
    background: var(--canvas-bg);
  }
  .canvas {
    position: relative;
    width: 1002px;
    height: 1200px;
  }
  .cap {
    position: absolute;
    left: 397px;
    top: 127px;
    width: 221px;
    height: 465px;
    background: var(--cap-black);
    border-radius: 4px 4px 0 0;
  }
  .cap-line {
    position: absolute;
    left: 0;
    width: 100%;
    height: 2px;
    background: var(--cap-line);
  }
  .cap-line--upper { top: 443px; }
  .cap-line--lower { top: 458px; }
  .bottle-front {
    position: absolute;
    left: 325px;
    top: 592px;
    width: 360px;
    height: 486px;
    background: linear-gradient(180deg, var(--body-pink) 0%, var(--body-pink-light) 55%, var(--body-pink) 100%);
    border-radius: 6px;
  }
  .brand-name {
    position: absolute;
    left: 0;
    top: 92px;
    width: 100%;
    margin: 0;
    text-align: center;
    font-family: "Kaushan Script", cursive;
    font-weight: 400;
    font-size: 150px;
    line-height: 1;
    color: var(--title-orange);
  }
  .ornament-band {
    position: absolute;
    left: 10px;
    top: 306px;
    width: 333px;
    height: 172px;
    background: linear-gradient(180deg,
      var(--band-purple) 0%,
      var(--band-coral) 20%,
      var(--band-coral) 38%,
      var(--band-teal) 48%,
      var(--body-pink-light) 62%,
      var(--band-purple) 80%,
      var(--band-orange) 100%);
  }
</style>
</head>
<body>
  <main class="canvas">
    <div class="cap">
      <span class="cap-line cap-line--upper"></span>
      <span class="cap-line cap-line--lower"></span>
    </div>
    <section class="bottle-front">
      <h1 class="brand-name">Vira</h1>
      <div class="ornament-band" role="img" aria-label="Festive folk border of dotted, wavy and zigzag bands in purple, coral, teal, white and orange"></div>
    </section>
  </main>
</body>
</html>
```